Pelican Litigation Funding Letterhead & Document Template

We need a letter head designed for our fund. Our fund works with law firms and investors across the globe. We need a a cover letter template as well as a document template for subsequent pages. Blue and white color scheme is preferred. This is our predecessor's website: https://www.pelicanvq.com/index.html. Please see our logo attached. The logo color code is #19478d. Font is Gotham-Medium.
Target Market(s)
Sophisticated investors and law firms
Font styles to use
Sans Serif
Colors
0255a3

```html
<!DOCTYPE html>
<html lang="en">
<head>
<meta charset="utf-8">
<title>Pelican Litigation Funding Letterhead</title>
<link rel="stylesheet" href="https://fonts.googleapis.com/css2?family=Poppins:wght@400;500&family=Tinos&display=swap">
<style>
  :root {
    --backdrop: #e4e5e7;
    --paper: #f9f9f9;
    --ink: #2c4f95;
    --brand: #19478d;
    --accent: #4a92c9;
    --rule: #3a5aa0;
  }
  * { box-sizing: border-box; margin: 0; padding: 0; }
  html, body { width: 1200px; height: 800px; overflow: hidden; }
  body { background: var(--backdrop); font-family: "Poppins", sans-serif; color: var(--ink); }

  .letterhead {
    position: absolute; left: 340px; top: 32px;
    width: 520px; height: 736px;
    background: var(--paper);
    box-shadow: 0 2px 6px rgba(0,0,0,.08);
    display: grid; grid-template-columns: 150px 1fr;
  }

  .sidebar {
    position: relative;
    border-right: 1px solid var(--rule);
    margin: 34px 0 28px;
    text-align: center;
    font-size: 7px; line-height: 1.5;
  }
  .brand { display: flex; flex-direction: column; align-items: center; gap: 6px; padding: 0 10px; }
  .brand-mark { width: 18px; height: 18px; border-radius: 50%; background: var(--brand); }
  .brand-name { font-weight: 500; font-size: 9.5px; line-height: 1.25; color: var(--brand); letter-spacing: .04em; text-transform: uppercase; }

  .contact { margin-top: 28px; display: flex; flex-direction: column; align-items: center; gap: 1px; }
  .contact + .contact { margin-top: 18px; }
  .icon { width: 13px; height: 13px; border-radius: 50%; background: var(--ink); display: grid; place-items: center; margin-bottom: 4px; }
  .icon svg { width: 8px; height: 8px; }

  .office { position: absolute; left: 0; right: 0; bottom: 6px; font-style: normal; }

  .letter { padding: 66px 30px 0 26px; font-size: 7.2px; line-height: 1.55; }
  .letter-date { text-align: right; }
  .recipient { text-align: right; margin-top: 18px; }
  .recipient-name { color: var(--accent); }
  .salutation { text-align: right; margin-top: 20px; color: var(--accent); font-size: 9.5px; font-weight: 400; letter-spacing: .06em; text-transform: uppercase; }
  .body-copy { margin-top: 10px; display: flex; flex-direction: column; gap: 16px; }
  .body-copy p { text-align: justify; text-align-last: right; }

  .sign-off { margin-top: 40px; width: 90px; text-align: center; }
  .signature { width: 42px; height: 30px; margin: 0 auto 4px; background: linear-gradient(135deg, #dfe4ef, #c9d2e6); border-radius: 3px; }
  .signer-name { font-family: "Tinos", serif; font-size: 10px; }
  .signer-role { font-family: "Tinos", serif; font-size: 7px; color: var(--accent); }
</style>
</head>
<body>
  <main class="letterhead">
    <aside class="sidebar">
      <div class="brand">
        <span class="brand-mark"></span>
        <span class="brand-name">Pelican Litigation Funding</span>
      </div>

      <div class="contact">
        <span class="icon"><svg viewBox="0 0 10 10"><path d="M2.2 1.2 3.6 1l.8 2-1 .8a5.5 5.5 0 0 0 2.8 2.8l.8-1 2 .8-.2 1.4c-.1.5-.6.8-1.1.7A7.8 7.8 0 0 1 1.4 2.3c-.1-.5.2-1 .8-1.1Z" fill="#fff"/></svg></span>
        <span>Tel: (555) 014-3815</span>
        <span>Fax: (555) 014-3816</span>
      </div>

      <div class="contact">
        <span class="icon"><svg viewBox="0 0 10 10" fill="none" stroke="#fff" stroke-width=".8"><circle cx="5" cy="5" r="3.8"/><ellipse cx="5" cy="5" rx="1.6" ry="3.8"/><path d="M1.2 5h7.6M1.8 3h6.4M1.8 7h6.4"/></svg></span>
        <span>Email: info@pelicanvq.com</span>
        <span>www.pelicanvq.com</span>
      </div>

      <address class="office contact">
        <span class="icon"><svg viewBox="0 0 10 10"><path d="M5 .8a3.3 3.3 0 0 0-3.3 3.3C1.7 6.5 5 9.2 5 9.2s3.3-2.7 3.3-5.1A3.3 3.3 0 0 0 5 .8Zm0 4.6a1.3 1.3 0 1 1 0-2.6 1.3 1.3 0 0 1 0 2.6Z" fill="#fff"/></svg></span>
        <span>Larkfield Court - Penthouse Floor</span>
        <span>1840 Meridian Avenue</span>
        <span>Suite 420, Brookvale, Nevada</span>
        <span>89012</span>
      </address>
    </aside>

    <section class="letter">
      <p class="letter-date">Wednesday, October 28, 2020</p>
      <p class="recipient">
        54 Heron Lane <span class="recipient-name">Corwin</span><br>
        32 Marlow Point<br>
        Ashford Vale
      </p>
      <h1 class="salutation">Dear Morgan</h1>

      <div class="body-copy">
        <p>Lorem ipsum dolor sit amet, cetero accusamus intellegat at his, usu aeterno erroribus sadipscing id, nam virtute equidem reprimique ea. Est cu modo oblique theophrastus, vix ex ferri dicam iisque, idque nostrud eam ut. Tation constituto repriique ut vis. Cu appareat dissentias qui. Vitae causae ceteros mea an, pro mutat admodum ex, ad quo commodo principes. Eam ignota impetus epicuri no, augue affert in vis. Pro nobis veteem eu, ex ius alia utamur explicari.</p>
        <p>Lorem ipsum dolor sit amet, cetero accusamus intellegat at his, usu aeterno erroribus sadipscing id, nam virtute equidem reprimique ea. Est cu modo oblique theophrastus, vix ex ferri dicam iisque, idque nostrud eam ut. Tation constituto repriique ut vis. Cu appareat dissentias qui.</p>
        <p>Tation constituto reprimique ut vis. Cu appareat dissentias qui. Vitae causae ceteros mea an, pro mutat admodum ex, ad quo commodo principes. Eam ignota impetus epicuri no,</p>
      </div>

      <div class="sign-off">
        <div class="signature" role="img" aria-label="Handwritten signature"></div>
        <p class="signer-name">Enter Your Name</p>
        <p class="signer-role">Lawyer</p>
      </div>
    </section>
  </main>
</body>
</html>
```